Investigation Tool App - Static Google Ad Image

We need a static image design that promotes our website, which provides an online incident investigation collaboration tool. I would like this static image for Google, but I am also seeking the same design in a LinkedIn Ad ratio.

We would like to see engaging ad graphics that capture the essence of collaboration, time saving, fast "impact-to-learnings" type vibe. As it helps them collaborate and facilitate the investigation on our interactive canvas and then it has an automated report builder that is AI-assisted to turn their information into coherent sentences in the report, it is not fully AI generated (this is important as i feel people inherently distrust AI generated content).

This tool is aimed at safety professionals in mining, construction and oil & gas who want an easy way to facilitate investigations virtually or in person without having to use whiteboards and double handle information and that want to be able to generate a report and learnings on the same day to quickly prevent further harm.

I have included a bunch of snips of my site and features etc - please feel free to use any of them but dont be constrained by these.

Target Market(s)

Safety Professionals/ Managers in Mining, Oil & Gas & Construction

Industry/Entity Type

Mining, Oil & Gas & Construction

Font styles to use
Sans Serif

Requirements
Nice to have
• Modern, pain point focussed, visual of investigation map and or nodes
Should not have
• No em-dashes, no gimmicky language or terms

```html
<!DOCTYPE html>
<html lang="en">
<head>
<meta charset="utf-8">
<title>Investigate Together. Act Sooner.</title>
<link rel="stylesheet" href="https://fonts.googleapis.com/css2?family=Outfit:wght@300;400;500;600;800&display=swap">
<style>
  :root {
    --ink: #0e1a12;
    --green: #27c35c;
    --button: #4fdc86;
    --dark: #0b1510;
    --mint: #eafbef;
    --paper: #ffffff;
    --line-green: #3fd872;
  }
  * { box-sizing: border-box; margin: 0; padding: 0; }
  html, body { width: 1200px; height: 628px; overflow: hidden; }
  body { font-family: "Outfit", Arial, sans-serif; color: var(--ink); background: var(--mint); }
  .ad { position: relative; width: 1200px; height: 628px; overflow: hidden; }
  .ad__backdrop { position: absolute; inset: 0; }
  .ad__copy { position: absolute; left: 58px; top: 150px; width: 520px; }
  .headline { font-weight: 800; }
  .headline__lead { display: block; font-size: 46px; font-weight: 800; letter-spacing: -0.3px; line-height: 1; }
  .headline__accent { display: block; font-size: 78px; font-weight: 800; color: var(--green); letter-spacing: -0.5px; line-height: 1; margin-top: 10px; }
  .subline { font-size: 29px; font-weight: 300; line-height: 1.4; margin-top: 22px; }
  .subline strong { color: var(--green); font-weight: 800; }
  .cta { position: absolute; left: 60px; top: 422px; width: 280px; height: 60px; border-radius: 10px; background: var(--button);
         display: flex; align-items: center; justify-content: center; font-size: 24px; font-weight: 400; color: var(--ink); text-decoration: none; }
  .board { position: absolute; left: 604px; top: 206px; width: 596px; height: 362px; overflow: visible; }
</style>
</head>
<body>
<main class="ad">
  <svg class="ad__backdrop" width="1200" height="628" viewBox="0 0 1200 628" aria-hidden="true">
    <defs>
      <linearGradient id="mintWash" x1="0" y1="0" x2="1" y2="0">
        <stop offset="0" stop-color="#f3fdf6"/>
        <stop offset="0.55" stop-color="#d9f7e3"/>
        <stop offset="1" stop-color="#8fe8ad"/>
      </linearGradient>
      <linearGradient id="edgeGlow" x1="0" y1="0" x2="1" y2="0">
        <stop offset="0" stop-color="#5fe394" stop-opacity="0"/>
        <stop offset="1" stop-color="#3fd872"/>
      </linearGradient>
    </defs>
    <rect width="1200" height="628" fill="url(#mintWash)"/>
    <path d="M700 0 C640 220 540 430 420 628 L520 628 C620 420 720 220 790 0 Z" fill="url(#edgeGlow)"/>
    <path d="M790 0 C720 220 620 420 520 628 L1200 628 L1200 0 Z" fill="var(--dark)"/>
    <path d="M780 0 C710 220 610 420 510 628" fill="none" stroke="#3fd872" stroke-width="10"/>
    <path d="M862 0 C848 14 838 26 829 38 C760 150 610 320 470 628" fill="none" stroke="#ffffff" stroke-width="3"/>
    <path d="M960 0 C920 50 900 90 882 118 C780 260 580 340 570 418 C565 480 562 560 560 628" fill="none" stroke="#3fd872" stroke-width="2"/>
    <g fill="#ffffff" stroke="#3fd872" stroke-width="3">
      <circle cx="829" cy="38" r="7"/>
      <circle cx="882" cy="118" r="7"/>
      <circle cx="570" cy="418" r="7"/>
      <circle cx="562" cy="598" r="7"/>
    </g>
  </svg>

  <section class="ad__copy">
    <h1 class="headline">
      <span class="headline__lead">Investigate Together.</span>
      <span class="headline__accent">Act Sooner.</span>
    </h1>
    <p class="subline">Turn findings into clear, structured reports <strong>in minutes.</strong></p>
  </section>

  <a class="cta" href="#">See How It Works</a>

  <svg class="board" viewBox="0 0 596 362" aria-label="Investigation map workspace">
    <defs>
      <pattern id="gridLines" width="10" height="10" patternUnits="userSpaceOnUse">
        <path d="M10 0H0V10" fill="none" stroke="#e6ebe7" stroke-width="0.6"/>
      </pattern>
      <linearGradient id="toolPurple" x1="0" y1="0" x2="1" y2="1">
        <stop offset="0" stop-color="#ff4fa3"/><stop offset="1" stop-color="#5b4dff"/>
      </linearGradient>
      <radialGradient id="lensGlass" cx="0.5" cy="0.5" r="0.5">
        <stop offset="0.7" stop-color="#ffffff" stop-opacity="0.95"/>
        <stop offset="1" stop-color="#dfe6e2" stop-opacity="0.9"/>
      </radialGradient>
    </defs>
    <rect x="0" y="0" width="596" height="362" rx="6" fill="var(--paper)"/>
    <rect x="0" y="26" width="596" height="336" fill="url(#gridLines)"/>
    <rect x="0" y="0" width="596" height="26" fill="#0d0d0d"/>
    <text x="14" y="18" font-family="Outfit, Arial, sans-serif" font-weight="600" font-size="14" letter-spacing="1" fill="#ffffff">TRACE</text>
    <text x="84" y="17" font-family="Outfit, Arial, sans-serif" font-size="8" font-weight="500" letter-spacing="1.5" fill="#3fd872">INVESTIGATION MAP</text>

    <rect x="18" y="36" width="22" height="22" rx="4" fill="#fff" stroke="#e0e0e0"/>
    <path d="M33 47H24M27 43L23 47L27 51" stroke="#111" stroke-width="1.6" fill="none"/>
    <rect x="18" y="64" width="22" height="22" rx="4" fill="url(#toolPurple)"/>
    <path d="M24 80L33 70" stroke="#fff" stroke-width="1.5"/>

    <g font-family="Outfit, Arial, sans-serif" font-size="4" fill="#333">
      <rect x="70" y="76" width="426" height="62" rx="4" fill="none" stroke="#999" stroke-width="0.7"/>
      <text x="76" y="81">Incident Sequence</text>
      <rect x="100" y="90" width="46" height="38" fill="#fff" stroke="#ddd"/><rect x="100" y="90" width="46" height="5" fill="#cfe0ff"/><rect x="100" y="123" width="46" height="5" fill="#111"/>
      <rect x="180" y="90" width="46" height="38" fill="#fff" stroke="#ddd"/><rect x="180" y="90" width="46" height="5" fill="#cfe0ff"/><rect x="180" y="123" width="46" height="5" fill="#111"/>
      <rect x="260" y="90" width="46" height="38" fill="#fff" stroke="#ddd"/><rect x="260" y="90" width="46" height="5" fill="#cfe0ff"/><rect x="260" y="123" width="46" height="5" fill="#111"/>
      <g stroke="#bbb" stroke-width="1.2"><path d="M105 102H141M105 107H138M105 112H140M185 102H221M185 107H218M185 112H220M265 102H301M265 107H298M265 112H300"/></g>
      <rect x="340" y="90" width="46" height="38" fill="#f1f1f1"/>
      <rect x="512" y="76" width="84" height="62" rx="4" fill="none" stroke="#bbb" stroke-width="0.7"/>

      <rect x="70" y="144" width="128" height="112" rx="4" fill="none" stroke="#999" stroke-width="0.7"/>
      <text x="76" y="149">Involved People</text>
      <g fill="#111"><circle cx="106" cy="172" r="12"/><circle cx="165" cy="172" r="12"/><circle cx="106" cy="222" r="12"/><circle cx="165" cy="222" r="12"/></g>
      <g stroke="#bbb" stroke-width="1.2"><path d="M91 190H121M150 190H180M91 240H121M150 240H180"/></g>

      <rect x="208" y="144" width="86" height="112" rx="4" fill="none" stroke="#999" stroke-width="0.7"/>
      <text x="214" y="149">Facts</text>
      <rect x="224" y="158" width="46" height="40" fill="#fff" stroke="#ddd"/><rect x="224" y="158" width="46" height="5" fill="#ff9a3d"/><rect x="224" y="192" width="46" height="6" fill="#ffe2e2"/>
      <rect x="224" y="208" width="46" height="40" fill="#fff" stroke="#ddd"/><rect x="224" y="208" width="46" height="5" fill="#ff9a3d"/><rect x="224" y="242" width="46" height="6" fill="#ffe2e2"/>
      <g stroke="#bbb" stroke-width="1.2"><path d="M229 170H265M229 176H262M229 182H264M229 220H265M229 226H262M229 232H264"/></g>

      <rect x="298" y="144" width="198" height="112" rx="4" fill="none" stroke="#999" stroke-width="0.7"/>
      <text x="304" y="149">Identified Factors</text>
      <rect x="310" y="158" width="46" height="40" fill="#fff" stroke="#ddd"/><rect x="310" y="158" width="46" height="5" fill="#ffd84d"/>
      <rect x="370" y="158" width="46" height="40" fill="#fff" stroke="#ddd"/><rect x="370" y="158" width="46" height="5" fill="#ffd84d"/>
      <rect x="430" y="158" width="46" height="40" fill="#fff" stroke="#ddd"/><rect x="430" y="158" width="46" height="5" fill="#ffd84d"/>
      <rect x="310" y="208" width="46" height="40" fill="#fff" stroke="#ddd"/><rect x="310" y="208" width="46" height="5" fill="#b79cff"/>
      <rect x="370" y="208" width="46" height="40" fill="#fff" stroke="#ddd"/><rect x="370" y="208" width="46" height="5" fill="#b79cff"/>
      <rect x="430" y="208" width="46" height="40" fill="#fff" stroke="#ddd"/><rect x="430" y="208" width="46" height="5" fill="#b79cff"/>
      <g stroke="#bbb" stroke-width="1.2"><path d="M315 170H351M315 176H348M375 170H411M375 176H408M435 170H471M435 176H468M315 220H351M315 226H348M375 220H411M375 226H408M435 220H471M435 226H468"/></g>
      <g fill="#e8f5ea"><rect x="313" y="188" width="40" height="5"/><rect x="373" y="188" width="40" height="5"/><rect x="433" y="188" width="40" height="5"/><rect x="313" y="238" width="40" height="5"/><rect x="373" y="238" width="40" height="5"/><rect x="433" y="238" width="40" height="5"/></g>

      <rect x="506" y="144" width="90" height="112" rx="4" fill="none" stroke="#999" stroke-width="0.7"/>
      <rect x="520" y="158" width="50" height="30" fill="#fff" stroke="#ddd"/><rect x="520" y="158" width="50" height="5" fill="#4fdc86"/>
      <rect x="520" y="208" width="50" height="30" fill="#fff" stroke="#ddd"/><rect x="520" y="208" width="50" height="5" fill="#4fdc86"/>
      <g stroke="#bbb" stroke-width="1.2"><path d="M525 170H565M525 176H560M525 220H565M525 226H560"/></g>

      <rect x="70" y="266" width="128" height="72" rx="4" fill="none" stroke="#999" stroke-width="0.7"/>
      <text x="76" y="271">Incident Outcome</text>
      <rect x="84" y="280" width="46" height="44" fill="#fff" stroke="#ddd"/><rect x="84" y="280" width="46" height="5" fill="#e52b2b"/>
      <rect x="140" y="280" width="46" height="44" fill="#fff" stroke="#ddd"/><rect x="140" y="280" width="46" height="5" fill="#e52b2b"/>
      <rect x="212" y="266" width="200" height="72" rx="4" fill="none" stroke="#999" stroke-width="0.7"/>
      <text x="218" y="271">Key Findings</text>
      <rect x="222" y="278" width="56" height="12" fill="#1f57e0"/><rect x="284" y="278" width="56" height="12" fill="#1f57e0"/><rect x="346" y="278" width="56" height="12" fill="#1f57e0"/>
      <rect x="424" y="266" width="172" height="72" rx="4" fill="none" stroke="#999" stroke-width="0.7"/>
      <text x="430" y="271">Recommendations</text>
      <rect x="440" y="280" width="52" height="36" fill="#fff" stroke="#ddd"/><rect x="440" y="280" width="52" height="5" fill="#4fdc86"/>
      <rect x="510" y="280" width="52" height="36" fill="#fff" stroke="#ddd"/><rect x="510" y="280" width="52" height="5" fill="#4fdc86"/>
      <g stroke="#bbb" stroke-width="1.2"><path d="M89 295H125M89 301H122M145 295H181M145 301H178M226 300H274M226 306H270M288 300H336M288 306H332M350 300H398M350 306H394M445 294H487M445 300H483M515 294H557M515 300H553"/></g>
    </g>

    <circle cx="411" cy="30" r="128" fill="#ffffff" fill-opacity="0.16" stroke="#ffffff" stroke-opacity="0.35"/>
    <circle cx="411" cy="30" r="104" fill="url(#lensGlass)"/>
    <g fill="#3fd872">
      <circle cx="366" cy="-11" r="9"/><rect x="388" y="-16" width="86" height="10" rx="5"/>
      <circle cx="366" cy="19" r="9"/><rect x="388" y="14" width="86" height="10" rx="5"/>
      <circle cx="366" cy="49" r="9"/><rect x="388" y="44" width="86" height="10" rx="5"/>
      <circle cx="366" cy="80" r="9"/><rect x="388" y="75" width="86" height="10" rx="5"/>
    </g>
    <path d="M536 108L596 64L596 130Z" fill="#3fd872"/>
  </svg>
</main>
</body>
</html>
```